Ad Design for a child care centre

Bright Pebbles Child Care Centre offers a safe, nurturing environment where your child will get the attention and care that he or she needs. Our ratio of children to adults is always within state guidelines - and often even higher - to make certain each child receives top-quality care
We are also state licensed as a Child Care facility and have met or exceeded all health and safety guidelines.
3-5 year Kinder Funded Program
Story Time
Show and Tell
Puzzles and Games
Computer Time
Arts and Crafts
Music
Pre-Reading Activities
And much more
You can rest assured that your child will be cared for with the most kindness, love and respect. We believe all children are precious gifts and we treat them as though they are our own.
Full-time, part-time, Half days, Before, after-school schedules are available.
To learn more, contact us today! 03 9514 -0817 or info@brightpebbles.example.au

```html
<!DOCTYPE html>
<html lang="en">
<head>
<meta charset="utf-8">
<title>Bright Pebbles Child Care Centre</title>
<link rel="stylesheet" href="https://fonts.googleapis.com/css2?family=Quicksand:wght@400;500;600;700&display=swap">
<style>
  :root {
    --purple: #8e2a8f;
    --purple-text: #8a3d8c;
    --cyan: #1ab1e8;
    --pink: #e3197f;
    --white: #ffffff;
    --ink: #1a1a1a;
    --grey: #555555;
  }
  * { margin: 0; padding: 0; box-sizing: border-box; }
  html, body { width: 1200px; height: 848px; overflow: hidden; background: var(--white); }
  body { font-family: "Quicksand", sans-serif; }
  .ad { position: relative; width: 1200px; height: 848px; background: var(--white); overflow: hidden; }

  .header-band { position: absolute; left: 0; top: 0; width: 1200px; height: 200px; }
  .ad-title {
    position: absolute; top: 22px; left: 0; width: 100%;
    text-align: center; color: var(--cyan);
    font-size: 56px; font-weight: 600; letter-spacing: 1px; line-height: 1.1;
  }
  .tagline {
    position: absolute; top: 90px; left: 0; width: 100%;
    text-align: center; color: var(--white);
    font-size: 28px; font-weight: 500; line-height: 41px; letter-spacing: 0.5px;
  }

  .intro {
    position: absolute; left: 28px; top: 164px; width: 705px;
    color: var(--purple-text); font-size: 20.5px; line-height: 29px; font-weight: 500;
  }
  .intro .name { font-style: italic; font-weight: 700; font-size: 24px; color: var(--purple); }
  .intro em { font-style: italic; }

  .photo { position: absolute; }
  .photo-playground { left: 27px; top: 420px; width: 234px; height: 236px; background: linear-gradient(160deg, #6aa0c0, #d88a8f 55%, #b5715f); }
  .photo-party { left: 271px; top: 420px; width: 235px; height: 236px; background: linear-gradient(170deg, #8a7a6a, #d488b8 50%, #5e7a3e); }
  .photo-baby { left: 516px; top: 420px; width: 224px; height: 150px; background: linear-gradient(150deg, #d6849a, #c9a7a0 55%, #f0c7cc); }
  .photo-group { left: 516px; top: 577px; width: 224px; height: 250px; background: linear-gradient(175deg, #7d8a6a, #c49a8a 50%, #8a4f7a); }

  .promise {
    position: absolute; left: 26px; top: 664px; width: 487px; height: 157px;
    background: var(--purple); color: var(--white);
    font-style: italic; font-weight: 600; font-size: 18.5px; line-height: 25.5px;
    text-align: center; padding: 20px 22px 0;
  }

  .activities {
    position: absolute; left: 748px; top: 180px; width: 450px;
    list-style: none; text-align: center;
    font-style: italic; font-weight: 700; font-size: 34px; line-height: 46px; letter-spacing: 0.5px;
  }
  .activities .cyan { color: var(--cyan); }
  .activities .purple { color: var(--purple); }
  .activities .pink { color: var(--pink); }

  .schedules {
    position: absolute; left: 805px; top: 556px; width: 324px; height: 132px;
    background: var(--pink); border-radius: 14px; color: var(--white);
    font-style: italic; font-weight: 600; font-size: 20px; line-height: 28px;
    text-align: center; padding-top: 10px;
  }

  .contact { position: absolute; left: 748px; top: 696px; width: 450px; text-align: center; }
  .contact-lead { color: var(--ink); font-weight: 700; font-size: 18px; letter-spacing: 0.5px; line-height: 26px; }
  .contact-phone { color: var(--purple); font-style: italic; font-weight: 700; font-size: 31px; letter-spacing: 2px; line-height: 40px; }
  .contact-email { color: var(--purple); font-style: italic; font-weight: 700; font-size: 26px; letter-spacing: 0.5px; line-height: 38px; }
  .contact-web { color: var(--grey); font-weight: 500; font-size: 19px; letter-spacing: 5px; line-height: 28px; }
</style>
</head>
<body>
<main class="ad">
  <svg class="header-band" viewBox="0 0 1200 200" aria-hidden="true">
    <path d="M0,0 H1200 V150 Q600,200 0,160 Z" fill="var(--purple)"/>
    <path d="M0,160 Q600,200 1200,150" fill="none" stroke="var(--pink)" stroke-width="5"/>
  </svg>
  <h1 class="ad-title">Bright Pebbles Child Care Centre</h1>
  <p class="tagline">We are not just a Child Care Centre<br>we are FAMILY</p>

  <div class="intro">
    <p><span class="name">Bright Pebbles<br>Child Care Centre</span> offers a <em>safe, nurturing environment</em> where your child will get the attention and care that he or she needs. Our ratio of children to adults is always within state guidelines - and often even higher - to make certain each child receives <em>top-quality care</em></p>
    <p>We are also state licensed as a Child Care facility and have met or exceeded all health and safety guidelines.</p>
  </div>

  <div class="photo photo-playground" role="img" aria-label="Photo of two young children playing on a playground"></div>
  <div class="photo photo-party" role="img" aria-label="Photo of children in fairy costumes at an outdoor party"></div>
  <div class="photo photo-baby" role="img" aria-label="Photo of a baby lying on a play mat"></div>
  <div class="photo photo-group" role="img" aria-label="Photo of a group of smiling children in a garden"></div>

  <p class="promise">You can rest assured that your child will be cared for with the most kindness, love and respect. We believe all children are precious gifts and we treat them as though they are our own.</p>

  <ul class="activities">
    <li class="cyan">Story Time</li>
    <li class="purple">Show and Tell</li>
    <li class="pink">Puzzles and Games</li>
    <li class="cyan">Computer Time</li>
    <li class="purple">Arts and Crafts</li>
    <li class="pink">Music</li>
    <li class="cyan">Pre-Reading Activities</li>
    <li class="purple">and Much More</li>
  </ul>

  <p class="schedules">Full-time, part-time,<br>Half days,<br>Before &amp; After-school<br>schedules are available</p>

  <div class="contact">
    <p class="contact-lead">To learn more, contact us today!</p>
    <p class="contact-phone">03 9514 -0817</p>
    <p class="contact-email">info@brightpebbles.example.au</p>
    <p class="contact-web">www.brightpebbles.example.au</p>
  </div>
</main>
</body>
</html>
```